Marnie Lux Business Card Design

I need a business card for my daughter. She has it all described in the file below. But it needs to be square in shape. http://www.marnielux.com is her web site

Target Market(s)

18-35 year old women

Industry/Entity Type

Fashion

Contact Information for Business Card

Please look at the attached file as it has all the details.

Requirements
Must have
• Please look at the attached file as it has all the details.
Nice to have
Should not have

```html
<!DOCTYPE html>
<html lang="en">
<head>
<meta charset="utf-8">
<title>Marnie Lux Business Card</title>
<link href="https://fonts.googleapis.com/css2?family=Lato:wght@400&family=Cormorant+Garamond:wght@600&display=swap" rel="stylesheet">
<style>
  :root {
    --backdrop: #2b2b2d;
    --card-dark: #1f1f21;
    --marble-deep: #0d0c0a;
    --marble-vein: #4a3f22;
    --blush: #f8cddb;
    --ink: #1a1a1a;
    --white: #ffffff;
  }
  * { margin: 0; padding: 0; box-sizing: border-box; }
  html, body {
    width: 1200px; height: 800px; overflow: hidden;
    background: var(--backdrop);
  }
  .canvas {
    position: relative; width: 1200px; height: 800px;
    display: flex; justify-content: center; align-items: center; gap: 80px;
  }
  .card {
    position: relative; width: 460px; height: 460px;
    border-radius: 34px; overflow: hidden;
  }

  /* Front */
  .card--front { background: var(--marble-deep); }
  .marble-texture {
    position: absolute; inset: 0;
    background:
      radial-gradient(ellipse at 30% 25%, rgba(120,100,50,.45), transparent 45%),
      radial-gradient(ellipse at 75% 70%, rgba(110,92,45,.4), transparent 50%),
      linear-gradient(135deg, var(--marble-deep) 0%, var(--marble-vein) 50%, var(--marble-deep) 100%);
  }
  .brand-name {
    font-family: "Lato", sans-serif;
    font-weight: 400;
    line-height: 1;
    text-transform: uppercase;
  }
  .front-brand {
    position: absolute; left: 0; right: 0; top: 205px;
    text-align: center;
  }
  .front-brand .brand-name {
    font-size: 46px; letter-spacing: 6px; color: var(--blush);
  }

  /* Back */
  .card--back { background: var(--card-dark); }
  .back-panel {
    position: absolute; left: 26px; right: 26px; top: 26px; height: 320px;
    background: var(--blush);
  }
  .back-brand {
    position: absolute; right: 34px; top: 44px;
  }
  .back-brand .brand-name {
    font-size: 34px; letter-spacing: 4px; color: var(--ink);
  }

  .contact-list {
    position: absolute; left: 30px; top: 150px; list-style: none;
    font-family: "Lato", sans-serif; font-size: 19px; color: var(--ink);
    line-height: 26px;
  }
  .contact-item { display: flex; align-items: center; gap: 10px; }
  .contact-dot {
    width: 16px; height: 16px; border-radius: 50%; background: var(--white);
    flex: none;
  }
  .contact-label {
    width: 66px; flex: none;
    font-family: "Cormorant Garamond", serif; font-size: 13px;
    letter-spacing: 1px; color: var(--blush);
    background: var(--ink); padding: 0 4px; text-align: center; line-height: 18px;
  }

  .web-band {
    position: absolute; left: 26px; right: 26px; top: 346px; height: 62px;
    display: flex; align-items: center; padding-left: 34px;
    font-family: "Lato", sans-serif; font-size: 22px; letter-spacing: 1.5px;
    color: var(--blush);
  }
  .blush-strip {
    position: absolute; left: 26px; right: 26px; top: 408px; height: 14px;
    background: var(--blush);
  }
</style>
</head>
<body>
<main class="canvas">

  <section class="card card--front" aria-label="Card front">
    <div class="marble-texture" role="img" aria-label="Black marble texture with gold veins"></div>
    <div class="front-brand">
      <h1 class="brand-name">Marnie Lux</h1>
    </div>
  </section>

  <section class="card card--back" aria-label="Card back">
    <div class="back-panel">
      <div class="back-brand">
        <h2 class="brand-name">Marnie Lux</h2>
      </div>
      <ul class="contact-list">
        <li class="contact-item"><span class="contact-dot"></span>snapgram.com/marnieluxxo</li>
        <li class="contact-item"><span class="contact-dot"></span>chirper.com/marnieluxxo</li>
        <li class="contact-item"><span class="contact-dot"></span>@marnieluxxo</li>
        <li class="contact-item"><span class="contact-dot"></span>marnie@marnieluxxo</li>
        <li class="contact-item"><span class="contact-label">BLOG</span>marnielux.com</li>
        <li class="contact-item"><span class="contact-label">VIDTUBE</span>vidtube.com/marnielux</li>
      </ul>
    </div>
    <div class="web-band">www.marnielux.com</div>
    <div class="blush-strip"></div>
  </section>

</main>
</body>
</html>
```